MCP phase 1 web design

Meridale Capital Partners Ltd (MCP) is a challenger business to the traditional leasing market. We look for solutions to complex problems involving the funding of capital equipment within an office environment and then build documentation around the solution. We recently created a brief for a logo and successfully completed that assignment. We now need to create our first web site which is simply intended to be informative. To help interested designers we have attached a detailed brief that is broken into three sections. The first explains how we see the site developing over time from something quite straightforward initially to a full transaction capability. Whoever wins this competition will be expected to work with us into the future to help develop the site. Section 2 gives you a view about our likes and dislikes by reviewing some existing sites. Section 3 gives you the structure and content of the site based upon our likes and dislikes. We are by no means committed to the structure and if you believe it can be presented in a better way then please use your design. The text is fixed as content. The images to appear can be anything from photographs to line drawings again entirely at the designers whim. Currently we have a home page plus 5 subsidiary pages. A few things to help you:
1. The logo is fixed and should be amongst the downloads.
2. The colours we have are corporate and should be used.
3. The typeface we use within the business is "Verdana"
Good luck.

```html
<!DOCTYPE html>
<html lang="en">
<head>
<meta charset="utf-8">
<title>Meridale Capital Partners Ltd</title>
<link rel="stylesheet" href="https://fonts.googleapis.com/css2?family=PT+Sans:wght@400;700&family=PT+Sans+Narrow:wght@400;700&family=Noto+Sans:wght@400;700&display=swap">
<style>
:root{
  --blue:#1a6fc0;
  --blue-dark:#0f4f93;
  --grey-text:#666;
  --body-text:#333;
  --footer:#565656;
  --rule:#d9d9d9;
  --card-grey:#595959;
  --card-silver:#a9a9a9;
  --social:#c9d8f2;
}
*{margin:0;padding:0;box-sizing:border-box}
html,body{width:1200px;height:1000px;overflow:hidden}
body{
  position:relative;
  font-family:"Noto Sans",sans-serif;
  color:var(--body-text);
  background:linear-gradient(to bottom,#fff 0,#fff 110px,#e4eef8 220px,#9fc2e6 330px,#7eadde 410px,#b8d2ec 500px,#eef4fb 570px,#fff 620px,#fff 100%);
}
.top-bar{position:absolute;left:0;top:0;width:1200px;height:8px;background:#5a5a5a}
.brand{position:absolute;left:135px;top:40px;display:flex;align-items:center;gap:10px;
  font-family:"PT Sans",sans-serif;font-size:26px;color:var(--blue);line-height:1;white-space:nowrap}
.brand-mark{width:14px;height:14px;background:var(--blue)}
.main-nav{position:absolute;top:8px;left:0}
.nav-item{position:absolute;top:0;height:74px;border-left:1px solid var(--rule);
  font-family:"PT Sans",sans-serif;font-size:18px;color:var(--grey-text);white-space:nowrap}
.nav-item span{position:absolute;left:-1px;bottom:0;border-left:4px solid var(--blue);padding-left:10px;line-height:17px}
.hero{position:absolute;left:128px;top:121px;width:943px;height:395px;background:#fff;border:1px solid #c8c8c8;overflow:hidden}
.hero-photo{position:absolute;left:0;top:0;width:700px;height:393px;
  background:linear-gradient(to right,rgba(255,255,255,0) 60%,#fff 100%),linear-gradient(160deg,#d7e2ec 0%,#eef2f5 40%,#c9d4de 70%,#e9eef3 100%)}
.hero-title{position:absolute;left:290px;top:44px;font-family:"PT Sans Narrow",sans-serif;font-weight:400;font-size:30px;line-height:34px;color:var(--blue);white-space:nowrap;transform:scaleX(.86);transform-origin:left center}
.hero-text{position:absolute;left:298px;top:90px;width:610px;font-size:15.5px;line-height:20px;color:#2c2c2c}
.checklist{position:absolute;left:636px;top:164px;list-style:none}
.checklist li{display:flex;align-items:center;gap:12px;height:27px;font-size:14px;color:#555}
.btn-learn{position:absolute;left:639px;top:314px;width:216px;height:47px;border-radius:24px;
  background:linear-gradient(#3a8ad6,#1260b3);color:#fff;font-family:"PT Sans",sans-serif;font-weight:700;font-size:18px;
  display:flex;align-items:center;padding-left:28px;box-shadow:0 10px 8px -6px rgba(0,0,0,.25)}
.btn-learn .arrow{position:absolute;right:18px;top:10px}
.hero-shadow{position:absolute;left:150px;top:516px;width:900px;height:40px;background:radial-gradient(ellipse at top,rgba(40,70,110,.35),rgba(40,70,110,0) 70%)}
.card{position:absolute;top:570px;width:294px;height:199px;background:#fff;border:1px solid #c8c8c8}
.card-icon{position:absolute;left:0;top:19px;width:67px;height:58px;display:flex;align-items:center;justify-content:center}
.card-edge{position:absolute;right:0;top:19px;width:4px;height:58px}
.card-title{position:absolute;left:77px;top:13px;font-family:"PT Sans Narrow",sans-serif;font-weight:400;font-size:25px;line-height:31px;color:#222;white-space:nowrap}
.card-text{position:absolute;left:18px;top:86px;width:258px;font-size:12.3px;line-height:14.4px;color:#222}
.card-link{position:absolute;left:18px;top:169px;font-size:12.5px;color:var(--blue)}
.card--managed .card-icon,.card--managed .card-edge{background:var(--blue)}
.card--public .card-icon,.card--public .card-edge{background:var(--card-grey)}
.card--education .card-icon,.card--education .card-edge{background:var(--card-silver)}
.video-cta{position:absolute;left:317px;top:796px;font-family:"PT Sans Narrow",sans-serif;font-weight:400;font-size:27px;line-height:32px;color:var(--blue);white-space:nowrap;transform:scaleX(.84);transform-origin:left center}
.btn-video{position:absolute;left:672px;top:790px;width:191px;height:48px;border-radius:24px;background:linear-gradient(#3a8ad6,#1260b3);
  color:#fff;font-family:"PT Sans",sans-serif;font-weight:700;font-size:18px;display:flex;align-items:center;padding-left:69px;box-shadow:0 10px 8px -6px rgba(0,0,0,.25)}
.btn-video svg{position:absolute;left:0;top:0}
.footer{position:absolute;left:99px;top:858px;width:1000px;height:142px;background:var(--footer);border-top:4px solid var(--blue);color:#fff}
.quick-label{position:absolute;left:14px;top:2px;width:38px;height:100px;background:#4a4a4a;box-shadow:3px 0 4px rgba(0,0,0,.3)}
.quick-label span{position:absolute;left:6px;top:96px;transform:rotate(-90deg);transform-origin:left top;font-family:"PT Sans Narrow",sans-serif;font-weight:700;font-size:22px;line-height:26px;white-space:nowrap}
.footer-links{position:absolute;top:12px;list-style:none;font-size:11.5px;line-height:18px}
.social{position:absolute;left:469px;top:18px;display:flex;gap:7px}
.social span{width:30px;height:30px;border-radius:50%;background:var(--social)}
.footer-brand{position:absolute;left:752px;top:20px;display:flex;align-items:center;gap:8px;font-family:"PT Sans",sans-serif;font-size:16px;line-height:20px;color:#1d2a3a;white-space:nowrap}
.footer-brand .brand-mark{width:10px;height:10px;background:#1d2a3a}
.footer-note{position:absolute;left:776px;top:58px;font-size:11.5px;white-space:nowrap}
.copyright{position:absolute;left:693px;top:110px;font-size:12.5px;white-space:nowrap}
</style>
</head>
<body>
<div class="top-bar"></div>

<header>
  <div class="brand"><span class="brand-mark"></span>Meridale Capital Partners Ltd</div>
  <nav class="main-nav">
    <div class="nav-item" style="left:636px;width:194px"><span>Why Alternative ?</span></div>
    <div class="nav-item" style="left:830px;width:139px"><span>Solutions</span></div>
    <div class="nav-item" style="left:969px;width:100px"><span>Contact Us</span></div>
  </nav>
</header>

<section class="hero">
  <div class="hero-photo" role="img" aria-label="Photo of a hand using a calculator over printed financial charts on an office desk"></div>
  <h1 class="hero-title">CHALLENGER BUSINESS TO THE TRADITIONAL LEASING MARKET.</h1>
  <p class="hero-text">We look for solutions to complex problems involving the funding of capital equipment within an office environment and then build documentation around the solution.</p>
  <ul class="checklist">
    <li><svg width="20" height="16" viewBox="0 0 20 16"><path d="M1 8 L7 14 L19 2 L16 0 L7 9 L4 5 Z" fill="#1a6fc0"/></svg>Fee calculators</li>
    <li><svg width="20" height="16" viewBox="0 0 20 16"><path d="M1 8 L7 14 L19 2 L16 0 L7 9 L4 5 Z" fill="#1a6fc0"/></svg>Stats</li>
    <li><svg width="20" height="16" viewBox="0 0 20 16"><path d="M1 8 L7 14 L19 2 L16 0 L7 9 L4 5 Z" fill="#1a6fc0"/></svg>Case Studies</li>
    <li><svg width="20" height="16" viewBox="0 0 20 16"><path d="M1 8 L7 14 L19 2 L16 0 L7 9 L4 5 Z" fill="#1a6fc0"/></svg>PR and awards</li>
  </ul>
  <div class="btn-learn">Learn More
    <svg class="arrow" width="26" height="26" viewBox="0 0 26 26"><circle cx="13" cy="13" r="12" fill="#0d3f78"/><path d="M11 8 L16 13 L11 18 Z" fill="#fff"/></svg>
  </div>
</section>
<div class="hero-shadow"></div>

<section class="card card--managed" style="left:130px">
  <div class="card-icon"><svg width="46" height="40" viewBox="0 0 46 40"><g fill="#fff"><circle cx="16" cy="26" r="10"/><circle cx="33" cy="13" r="8"/></g><g fill="#1a6fc0"><circle cx="16" cy="26" r="4"/><circle cx="33" cy="13" r="3"/></g></svg></div>
  <div class="card-edge"></div>
  <h2 class="card-title">Managed Services<br>Solutions</h2>
  <p class="card-text">We look for solutions to complex problems involving the funding of capital equipment within an office environment and then build documentation around the solution</p>
  <a class="card-link">Learn More</a>
</section>
<section class="card card--public" style="left:451px">
  <div class="card-icon"><svg width="40" height="40" viewBox="0 0 40 40"><g fill="#fff"><rect x="13" y="4" width="14" height="16" rx="6"/><path d="M4 38 Q6 24 20 23 Q34 24 36 38 Z"/></g></svg></div>
  <div class="card-edge"></div>
  <h2 class="card-title">Public Sector<br>Solutions</h2>
  <p class="card-text">We look for solutions to complex problems involving the funding of capital equipment within an office environment and then build documentation around the solution</p>
  <a class="card-link">Learn More</a>
</section>
<section class="card card--education" style="left:773px">
  <div class="card-icon"><svg width="46" height="38" viewBox="0 0 46 38"><path d="M3 6 Q13 2 22 7 L22 35 Q13 30 3 34 Z M43 6 Q33 2 24 7 L24 35 Q33 30 43 34 Z" fill="#fff"/></svg></div>
  <div class="card-edge"></div>
  <h2 class="card-title">Education<br>Solutions</h2>
  <p class="card-text">We look for solutions to complex problems involving the funding of capital equipment within an office environment and then build documentation around the solution</p>
  <a class="card-link">Learn More</a>
</section>

<div class="video-cta">View Our Video Presentation Of Products</div>
<div class="btn-video">
  <svg width="52" height="48" viewBox="0 0 52 48"><circle cx="24" cy="24" r="22" fill="#1f73c8" stroke="#0e4f92" stroke-width="3"/><path d="M19 14 L33 24 L19 34 Z" fill="#fff"/></svg>
  Click here
</div>

<footer class="footer">
  <div class="quick-label"><span>Quick Links</span></div>
  <ul class="footer-links" style="left:78px">
    <li>Fee calculators</li><li>Stats</li><li>Case Studies</li><li>PR and awards</li><li>FAQ</li>
  </ul>
  <ul class="footer-links" style="left:260px">
    <li>Home</li><li>About Us</li><li>Why Alternative</li><li>Solustion</li><li>Contact Us</li>
  </ul>
  <div class="social" aria-label="Social media links"><span></span><span></span><span></span></div>
  <div class="footer-brand"><span class="brand-mark"></span>Meridale Capital Partners Ltd</div>
  <p class="footer-note">space for company details etc</p>
  <p class="copyright">©2014 Meridale Capital Partners Ltd</p>
</footer>
</body>
</html>
```